Book Cover Design (Front & Back)

I am looking to perfect & improve current design of my Book:

Count on me, the peddler ...

This book is about the good and the bad way of selling, in short the wolf sells because he is greedy and doesn't care, the dog sells, because he is looking to add value.

I like the current design, it's just that no attention to font and spacing and design elements have been given.

The current size is: 5.5" x 8.5" (13.97 x 21.59 cm)
Updates

Still open to receive concepts, and I will switch to guaranteeing that I will select one ...

Target Market(s)

Sales People, Entrepreneurs, Self-employed

Industry/Entity Type

Sales

Font styles to use
Sans Serif

Colors

Designer to choose colors to be used in the design.

Requirements
Must have
• Must have is:
• - The title: Count on me, the Peddler
• - the attached badge (idea: like it is stamped on the cover)
• - the subtitle: why loyal buyers stay with you over years of care
• - the photo on the back
• - Space for isbn barcodes the back
• - the text (explanation and the piece about the author)
• - the additional mention of 96.000 hours of training, etc.
• THIS WAS THE IDEA I HAD BUT NOW I AM NOT SO SURE:
• The DOG BADGE is now taking too much attention, it would be great to have this badge redesign it into a stamp, as in saying it is quality ... see attachment regarding stamp or make the badge into a wax seal ... that might also be an option
• NEW TEXT FOR ON THE BACK:
• Do you want to be a Sales Wolf or a Prime Deal Hawk?
• The Sales Wolf desperately chases customers every moment of the day. Sell, sell, sell! Customers are skeptical about the Sales Wolf and will avoid doing business with him as much as possible.
• The Sales Dog has customers waiting on his doorstep, asking to buy, as they are convinced that doing business with the Sales Dog will help them to be more successful and achieve their objectives!
• Apply the right mindset, so that you become the Prime Deal Hawk in your industry, region, or division by mastering the power of trust and value.
• Lenn ter Moorhaven is an internationally acclaimed author, speaker, and trainer with over 20 years of sales experience. Lenn has trained more than 10,000 sales professionals, transforming them into Prime Deal Hawks by placing the customer front and center in their buying process.
• Learn more about sales success through trust and value:
• www.primedealhawks.net
• www.lenntermoor.net
Nice to have
• Good colour
• Nice typography
• Nice spacing
• Great design elements on the back
• PLEASE NOTE: The current quotes are samples, and not real ones (yet)
Should not have
• no other pictures
• or change of texts

```html
<!DOCTYPE html>
<html lang="en">
<head>
<meta charset="utf-8">
<title>Count on Me, the Peddler — Front Cover</title>
<link href="https://fonts.googleapis.com/css2?family=Italianno&family=Cormorant+SC:wght@600;700&family=Cormorant+Garamond:ital,wght@0,600;0,700;1,700&display=swap" rel="stylesheet">
<style>
  :root {
    --red-deep: #a11a1f;
    --red-mid: #b3262c;
    --red-glow: #c4454b;
    --gold-line: #d08a36;
    --band-orange: #b96a2a;
    --seal-red: #b0181e;
    --seal-orange: #d98a3e;
    --ink-white: #ffffff;
    --shadow-dark: #2a0506;
  }
  html, body {
    margin: 0;
    padding: 0;
    width: 800px;
    height: 1200px;
    overflow: hidden;
    background: var(--red-deep);
  }
  .cover {
    position: relative;
    width: 800px;
    height: 1200px;
    box-sizing: border-box;
    border: 3px solid var(--gold-line);
    background: radial-gradient(ellipse 70% 55% at 50% 45%, var(--red-glow) 0%, var(--red-mid) 45%, var(--red-deep) 100%);
    overflow: hidden;
  }
  .praise-bar {
    position: absolute;
    left: 0; top: 0;
    width: 100%;
    height: 110px;
    background: var(--red-deep);
    border-bottom: 1px solid var(--gold-line);
  }
  .praise-quote {
    position: absolute;
    top: 16px;
    left: 0; width: 100%;
    text-align: center;
    font-family: "Cormorant Garamond", serif;
    font-style: italic;
    font-weight: 700;
    font-size: 36px;
    line-height: 44px;
    color: var(--ink-white);
    margin: 0;
  }
  .praise-source {
    position: absolute;
    top: 64px;
    right: 98px;
    font-family: "Cormorant Garamond", serif;
    font-weight: 600;
    font-size: 32px;
    line-height: 36px;
    color: var(--ink-white);
    margin: 0;
  }
  .rule {
    position: absolute;
    left: 0; width: 100%;
    height: 1px;
    background: var(--gold-line);
  }
  .rule-top { top: 122px; }
  .rule-bottom { top: 1072px; }
  .title {
    position: absolute;
    left: 0; top: 130px;
    width: 100%;
    margin: 0;
    text-align: center;
    color: var(--ink-white);
    font-weight: normal;
  }
  .title-script {
    display: block;
    font-family: "Italianno", cursive;
    font-size: 150px;
    line-height: 150px;
    text-shadow: 3px 3px 0 var(--shadow-dark);
  }
  .title-caps {
    display: block;
    margin-top: 8px;
    font-family: "Cormorant SC", serif;
    font-weight: 700;
    font-size: 112px;
    line-height: 112px;
    letter-spacing: -1px;
    text-shadow: 4px 3px 0 var(--shadow-dark);
  }
  .seal-area {
    position: absolute;
    left: 200px; top: 478px;
    width: 424px; height: 416px;
    border-radius: 50%;
    background: radial-gradient(circle at 50% 50%, var(--seal-orange) 0%, var(--seal-orange) 52%, var(--seal-red) 70%, var(--seal-red) 100%);
  }
  .subtitle-band {
    position: absolute;
    left: 0; top: 940px;
    width: 100%;
    height: 108px;
    background: var(--band-orange);
    box-shadow: 0 4px 10px rgba(0,0,0,0.35), 0 -4px 10px rgba(0,0,0,0.25);
    display: flex;
    align-items: center;
    justify-content: center;
  }
  .subtitle {
    margin: 0;
    white-space: nowrap;
    font-family: "Cormorant Garamond", serif;
    font-style: italic;
    font-weight: 700;
    font-size: 32px;
    text-transform: uppercase;
    color: var(--ink-white);
    text-shadow: 1px 1px 1px var(--shadow-dark);
    transform: scaleX(0.86);
  }
  .author {
    position: absolute;
    left: 0; top: 1110px;
    width: 100%;
    margin: 0;
    text-align: center;
    font-family: "Cormorant Garamond", serif;
    font-weight: 700;
    font-size: 48px;
    line-height: 56px;
    color: var(--ink-white);
    text-transform: uppercase;
    text-shadow: 2px 2px 0 var(--shadow-dark);
    transform: scaleX(0.68);
  }
</style>
</head>
<body>
  <main class="cover">
    <header class="praise-bar">
      <p class="praise-quote">‘Finally a Book That Shows the Heart of Selling’</p>
      <p class="praise-source">MARA T. QUILL</p>
    </header>
    <div class="rule rule-top"></div>

    <h1 class="title">
      <span class="title-script">Count on Me,</span>
      <span class="title-caps">The Peddler</span>
    </h1>

    <div class="seal-area" role="img" aria-label="Red wax seal stamped with the round customer-value badge illustration"></div>

    <div class="subtitle-band">
      <p class="subtitle">Why loyal buyers stay with you over years of care</p>
    </div>
    <div class="rule rule-bottom"></div>

    <p class="author">Lenn ter Moorhaven</p>
  </main>
</body>
</html>
```